Korvex Systems*

Stationary design including business cards, letter heads, envelops and email signatures using our new logo

Target Market(s)

Innovative Technologies

Industry/Entity Type

Defense Contracting

Font styles to use
Sans Serif

```html
<!DOCTYPE html>
<html lang="en">
<head>
<meta charset="utf-8">
<title>Korvex Systems — Stationery Set</title>
<link rel="stylesheet" href="https://fonts.googleapis.com/css2?family=Oswald:wght@400&family=Montserrat:ital,wght@0,400;0,500;0,600;1,500&family=Work+Sans:wght@400;500&display=swap">
<style>
  :root {
    --backdrop: #b5b5b5;
    --paper: #ffffff;
    --panel: #efefef;
    --flap: #f2f2f2;
    --ink: #111111;
    --ink-soft: #444444;
    --text-grey: #6a6a6a;
    --rule: #555555;
    --shadow: rgba(0,0,0,0.35);
  }
  * { box-sizing: border-box; margin: 0; padding: 0; }
  html, body { width: 1200px; height: 1044px; overflow: hidden; }
  body { background: var(--backdrop); position: relative; font-family: "Montserrat", sans-serif; color: var(--ink); }

  .sheet { position: absolute; background: var(--paper); box-shadow: 2px 3px 3px var(--shadow); }
  .wordmark { font-family: "Oswald", sans-serif; font-weight: 400; color: var(--ink); letter-spacing: 0.2px; white-space: nowrap; text-transform: uppercase; }

  /* Letterhead */
  .letterhead { left: 166px; top: 119px; width: 406px; height: 573px; }
  .letterhead .wordmark { position: absolute; top: 76px; left: 0; width: 100%; text-align: center; font-size: 13px; }
  .letter-greeting { position: absolute; left: 40px; top: 132px; font-size: 10px; font-weight: 500; color: var(--ink-soft); }
  .letter-body p { position: absolute; left: 40px; width: 326px; font-size: 5.6px; line-height: 10.2px; color: var(--text-grey); text-align: justify; }
  .letter-sender { position: absolute; left: 40px; top: 406px; }
  .letter-sender .name { font-size: 10px; font-style: italic; font-weight: 500; color: var(--ink-soft); }
  .letter-sender .role { font-size: 5.6px; font-style: italic; font-weight: 500; color: var(--ink-soft); }
  .signature-slot { position: absolute; left: 40px; top: 437px; width: 106px; height: 38px; background: linear-gradient(90deg, #f4f4f4, #e9e9e9); }
  .letter-rule { position: absolute; left: 40px; top: 514px; width: 326px; border-top: 1px solid var(--rule); }
  .letter-foot { position: absolute; top: 528px; font-size: 6.4px; line-height: 8.4px; color: var(--ink); }
  .letter-foot.contact { left: 40px; }
  .letter-foot.address { right: 40px; text-align: right; top: 536px; }
  .ico { display: inline-block; width: 6px; height: 6px; vertical-align: -1px; margin-right: 1px; }

  /* Business cards */
  .card { top: 119px; width: 205px; height: 117px; }
  .card-front { left: 613px; }
  .card-back { left: 829px; }
  .card-front .wordmark { position: absolute; left: 23px; top: 71px; font-size: 10.5px; }
  .card-divider { position: absolute; left: 95px; top: 32px; height: 53px; border-left: 1px solid var(--ink); }
  .card-info { position: absolute; left: 113px; top: 31px; font-size: 4.8px; line-height: 6.6px; color: var(--ink); }
  .card-info .name { font-size: 7px; font-weight: 600; letter-spacing: 0.3px; line-height: 8px; }
  .card-info .gap { height: 3px; }
  .card-back .wordmark { position: absolute; left: 0; width: 100%; text-align: center; top: 72px; font-size: 11px; }

  /* Envelope back */
  .envelope-back { left: 613px; top: 266px; width: 421px; height: 198px; overflow: hidden; }
  .envelope-back .flap { position: absolute; left: 0; top: 0; }
  .envelope-back .wordmark { position: absolute; left: 0; width: 100%; text-align: center; top: 16px; font-size: 19px; }

  /* Envelope front */
  .envelope-front { left: 613px; top: 495px; width: 421px; height: 197px; }
  .envelope-front .wordmark { position: absolute; left: 21px; top: 51px; font-size: 10.5px; }
  .envelope-front .address { position: absolute; left: 21px; top: 166px; font-size: 6.6px; line-height: 8.6px; }

  /* Email signature */
  .email-signature { left: 166px; top: 724px; width: 866px; height: 200px; display: flex; }
  .sig-contact { width: 194px; background: var(--paper); padding: 24px 0 0 28px; font-family: "Work Sans", sans-serif; }
  .sig-contact .name { font-size: 15px; font-weight: 500; letter-spacing: 0.6px; line-height: 18px; }
  .sig-contact .role { font-size: 11.5px; line-height: 14px; }
  .social { display: flex; gap: 7px; margin: 15px 0 12px; }
  .social span { width: 19px; height: 19px; border-radius: 3px; background: var(--ink); }
  .sig-contact .addr { font-size: 11.5px; line-height: 14.5px; margin-bottom: 5px; }
  .sig-contact .line { font-size: 11.5px; line-height: 14.5px; }
  .sig-contact .ico { width: 8px; height: 8px; margin-right: 3px; vertical-align: 0; }
  .sig-brand { flex: 1; background: var(--panel); position: relative; }
  .sig-brand .wordmark { position: absolute; left: 30px; top: 137px; font-size: 28px; }
</style>
</head>
<body>

<svg width="0" height="0" style="position:absolute">
  <defs>
    <symbol id="i-phone" viewBox="0 0 10 10"><path d="M2.5 1 L4 3.2 L3 4.2 Q4 6.2 5.8 7 L6.8 6 L9 7.5 L8 9 Q3.5 9 1 2 Z" fill="none" stroke="currentColor" stroke-width="1"/></symbol>
    <symbol id="i-mail" viewBox="0 0 10 10"><rect x="1" y="2.5" width="8" height="5.5" fill="none" stroke="currentColor" stroke-width="1"/><path d="M1 2.5 L5 5.6 L9 2.5" fill="none" stroke="currentColor" stroke-width="1"/></symbol>
    <symbol id="i-web" viewBox="0 0 10 10"><circle cx="5" cy="5" r="4" fill="none" stroke="currentColor" stroke-width="0.9"/><ellipse cx="5" cy="5" rx="1.8" ry="4" fill="none" stroke="currentColor" stroke-width="0.8"/><path d="M1 5 H9" stroke="currentColor" stroke-width="0.8"/></symbol>
  </defs>
</svg>

<section class="sheet letterhead">
  <div class="wordmark">Korvex Systems</div>
  <div class="letter-greeting">Dear sir/Madam,</div>
  <div class="letter-body">
    <p style="top:159px">Placeholder copy stands in for the final letter text and shows how a full page of writing will sit on this sheet. It has been set in the house body face at a modest size so that the reader can follow long passages with ease. The column keeps an even width from top to bottom and each line runs close to the same length, which gives the page a calm and ordered look that suits formal notes.</p>
    <p style="top:216px">Each paragraph is spaced apart to help the eye find its place, and the margins on both sides stay equal so the block reads as one clean panel. This sample will be swapped for real content when the letter is written and sent.</p>
    <p style="top:260px">Contrary to popular belief, sample text is not simply random words. It has roots in older writing from long ago, and a visiting scholar at a small college once traced a rare word through many texts to find its true source. That search showed how a passage can travel over time and change shape along the way. Writers and printers have used such passages for years to test type, spacing and layout before the final copy is ready. The first line of a sample is often the most familiar part of it, and many people know it by sight. It has kept its place in printing through many eras, from metal type to modern desktop tools, and it remains a quiet helper in design work. There are many versions of these passages, and most have been altered in</p>
    <p style="top:370px">some form, by added humour or shuffled words that do not look believable at all. If you plan to use a sample passage, be sure there is nothing awkward hidden in the middle</p>
  </div>
  <div class="letter-sender">
    <div class="name">Daniel Reyes</div>
    <div class="role">Director</div>
  </div>
  <div class="signature-slot" role="img" aria-label="Handwritten signature of the director"></div>
  <div class="letter-rule"></div>
  <div class="letter-foot contact">
    <div><svg class="ico"><use href="#i-phone"/></svg>555 014 2287</div>
    <div><svg class="ico"><use href="#i-mail"/></svg>info@korvexsystems.com</div>
    <div><svg class="ico"><use href="#i-web"/></svg>www.korvexsystems.com</div>
  </div>
  <div class="letter-foot address">
    <div>1480 Harbor Lane</div>
    <div>Fairview, OR 97024</div>
  </div>
</section>

<section class="sheet card card-front">
  <div class="wordmark">Korvex Systems</div>
  <div class="card-divider"></div>
  <div class="card-info">
    <div class="name">DANIEL REYES</div>
    <div>Founder</div>
    <div class="gap"></div>
    <div>1480 Harbor Lane</div>
    <div>Fairview, OR 97024</div>
    <div class="gap"></div>
    <div><svg class="ico" style="width:4.5px;height:4.5px"><use href="#i-phone"/></svg>555 014 2287</div>
    <div><svg class="ico" style="width:4.5px;height:4.5px"><use href="#i-mail"/></svg>info@korvexsystems.com</div>
    <div><svg class="ico" style="width:4.5px;height:4.5px"><use href="#i-web"/></svg>www.korvexsystems.com</div>
  </div>
</section>

<section class="sheet card card-back">
  <div class="wordmark">Korvex Systems</div>
</section>

<section class="sheet envelope-back">
  <svg class="flap" width="421" height="70" viewBox="0 0 421 70">
    <path d="M0 0 H421 L405 58 Q402 63 395 63 H26 Q19 63 17 58 Z" fill="var(--flap)" stroke="#cfcfcf" stroke-width="0.6"/>
  </svg>
  <div class="wordmark">Korvex Systems</div>
</section>

<section class="sheet envelope-front">
  <div class="wordmark">Korvex Systems</div>
  <div class="address">
    <div>1480 Harbor Lane</div>
    <div>Fairview, OR 97024</div>
  </div>
</section>

<section class="sheet email-signature">
  <div class="sig-contact">
    <div class="name">DANIEL REYES</div>
    <div class="role">Founder</div>
    <div class="social"><span></span><span></span></div>
    <div class="addr">1480 Harbor Lane<br>Fairview, OR 97024</div>
    <div class="line"><svg class="ico"><use href="#i-phone"/></svg>555 014 2287</div>
    <div class="line"><svg class="ico"><use href="#i-mail"/></svg>info@korvexsystems.com</div>
    <div class="line"><svg class="ico"><use href="#i-web"/></svg>www.korvexsystems.com</div>
  </div>
  <div class="sig-brand">
    <div class="wordmark">Korvex Systems</div>
  </div>
</section>

</body>
</html>
```